Business Card Design

Personal training studio. My colors are burnt orange and grey. Specializing in group training and total body composition change. Nutritional consultant and contest prep.

Target Market(s)

My audience are people who are looking for total body composition change as well as knowledge on how to effectively receive results in the gym that they are a member of.

Industry/Entity Type

Training

Contact Information for Business Card

Dr. Marla Petrov
Marlajpetrov@mailbox-example.com
3125550147
2817 east Bralen ave.
Brenmoor Westland 60999

Colors
f37122
aaaaaa

Requirements
Must have
• A focus on building knowledge that will carry them for a lifetime. Lasting results and visible results.
Nice to have
• Card should correlate with the colors of the studio. Orange and grey. With black flooring with orange speckles in it.

```html
<!DOCTYPE html>
<html lang="en">
<head>
<meta charset="utf-8">
<title>Kestrel Form Studio – Business Card</title>
<link rel="stylesheet" href="https://fonts.googleapis.com/css2?family=Arimo:wght@400;700&display=swap">
<style>
  :root {
    --page: #2b2b2b;
    --card-black: #1d1b1c;
    --panel-grey: #b4b4b4;
    --silver-light: #f2f2f2;
    --silver-dark: #6e6e6e;
    --orange: #f37122;
    --white: #ffffff;
    --ink: #111111;
  }
  * { box-sizing: border-box; margin: 0; padding: 0; }
  html, body {
    width: 1200px;
    height: 900px;
    overflow: hidden;
    background: var(--page);
    font-family: "Arimo", Arial, sans-serif;
  }
  .stage {
    width: 1200px;
    height: 900px;
    display: flex;
    flex-direction: column;
    align-items: center;
    justify-content: center;
    gap: 40px;
  }
  .card {
    position: relative;
    width: 700px;
    height: 400px;
    overflow: hidden;
    box-shadow: 0 12px 30px rgba(0,0,0,0.5);
  }

  /* Shared brand mark: dot plus name */
  .brand {
    position: absolute;
    display: flex;
    align-items: center;
    gap: 14px;
    color: var(--white);
    font-weight: 700;
    letter-spacing: 0.04em;
    text-transform: uppercase;
    white-space: nowrap;
  }
  .brand-dot {
    border-radius: 50%;
    background: var(--orange);
    flex: none;
  }

  /* Front */
  .card-front { background: var(--card-black); }
  .card-front .brand {
    left: 50%;
    top: 120px;
    transform: translateX(-50%);
    font-size: 30px;
  }
  .card-front .brand-dot { width: 56px; height: 56px; }
  .tagline {
    position: absolute;
    left: 0; right: 0;
    bottom: 34px;
    text-align: center;
    color: var(--white);
    font-weight: 700;
    font-size: 17px;
    line-height: 1.3;
  }

  /* Back */
  .card-back { background: var(--panel-grey); }
  .back-shape { position: absolute; inset: 0; }
  .card-back .brand {
    left: 36px;
    top: 178px;
    font-size: 20px;
  }
  .card-back .brand-dot { width: 44px; height: 44px; }
  .contact {
    position: absolute;
    left: 440px;
    top: 70px;
    color: var(--ink);
    font-size: 17px;
    line-height: 1.25;
    white-space: nowrap;
  }
  .contact-name { font-weight: 700; font-size: 18px; margin-bottom: 26px; }
  .contact-phone { margin-bottom: 22px; }
  .contact-address { margin-bottom: 22px; }
  .contact-email { font-size: 15px; }
</style>
</head>
<body>
  <main class="stage">
    <section class="card card-front">
      <div class="brand"><span class="brand-dot"></span>Kestrel Form Studio</div>
      <p class="tagline">A focus on building knowledge that will carry them for a lifetime.<br>Lasting results and visible results.</p>
    </section>

    <section class="card card-back">
      <svg class="back-shape" width="700" height="400" viewBox="0 0 700 400" aria-hidden="true">
        <defs>
          <linearGradient id="silver-band" x1="0" y1="0" x2="1" y2="0">
            <stop offset="0" stop-color="#6e6e6e"/>
            <stop offset="0.45" stop-color="#f2f2f2"/>
            <stop offset="1" stop-color="#6e6e6e"/>
          </linearGradient>
        </defs>
        <path d="M0 0 H350 C440 60 450 300 380 400 H0 Z" fill="url(#silver-band)"/>
        <path d="M0 0 H330 C420 60 430 300 360 400 H0 Z" fill="#1d1b1c"/>
      </svg>
      <div class="brand"><span class="brand-dot"></span>Kestrel Form Studio</div>
      <div class="contact">
        <p class="contact-name">Dr. Marla Petrov</p>
        <p class="contact-phone">3125550147</p>
        <p class="contact-address">2817 east Bralen ave.<br>Brenmoor Westland 60999</p>
        <p class="contact-email">Marlajpetrov@mailbox-example.com</p>
      </div>
    </section>
  </main>
</body>
</html>
```